Pet label template for Corvantis mexican based company

Hello, Corvantis is a mexican based company dedicated to manufacture and sell its propietary brands for human health care. We are now introducing a new "Pet" category to our Brand. It´s name is Corvantis Pets (logo attached).
We are lookoig for the design template for our package labels that will most probably be in plastic bags like the example attaches (Kindle Paw of lakeshire). It is important to point out that the labels are going to be pasted on the bags and not directly printed on the bags itself like the examples attached.

I am attaching some examples but please feel free to innovate your own desing. I am also attaching the logo that must be in every label.

Target Market(s)

Pet owners basically dogs and cats.

Industry/Entity Type

Health Care

Font styles to use
Other font styles liked:
• something easy to read

Requirements
Must have
• We like both simple elegant designs and bright colorful ones son feel free to innovate.
Nice to have
• Illustration of both cat or dog for their product label.

```html
<!DOCTYPE html>
<html lang="en">
<head>
<meta charset="utf-8">
<title>Corvantis Pets – Supplement for Cats Label</title>
<link rel="stylesheet" href="https://fonts.googleapis.com/css2?family=Nunito:wght@600;800;900&family=Quicksand:wght@500;600&display=swap">
<style>
  :root {
    --page-bg: #f4f5f6;
    --label-top: #c9d7e1;
    --label-mid: #eef3f6;
    --label-white: #ffffff;
    --brand-cyan: #1ea6d8;
    --wave-light: #8fd3ec;
    --wave-deep: #3bb3de;
    --brand-green: #2f8a3a;
    --body-text: #ffffff;
    --photo-a: #7b7d80;
    --photo-b: #c9c4bd;
  }
  * { box-sizing: border-box; margin: 0; padding: 0; }
  html, body {
    width: 878px;
    height: 1200px;
    overflow: hidden;
    background: var(--page-bg);
  }
  .label {
    position: absolute;
    left: 89px;
    top: 105px;
    width: 700px;
    height: 990px;
    border-radius: 14px;
    overflow: hidden;
    background: linear-gradient(180deg, var(--label-top) 0%, var(--label-mid) 30%, var(--label-white) 48%, var(--label-white) 100%);
    box-shadow: 0 2px 10px rgba(0,0,0,0.08);
  }
  .label__tagline {
    position: absolute;
    left: 0;
    top: 140px;
    width: 100%;
    text-align: center;
    font-family: "Quicksand", sans-serif;
    font-weight: 600;
    font-size: 40px;
    letter-spacing: 0.5px;
    color: var(--brand-cyan);
  }
  .label__title {
    position: absolute;
    left: 0;
    top: 200px;
    width: 100%;
    text-align: center;
    font-family: "Nunito", sans-serif;
    font-weight: 900;
    font-size: 92px;
    line-height: 0.86;
    letter-spacing: 1px;
    color: var(--brand-cyan);
  }
  .label__wave {
    position: absolute;
    left: 0;
    top: 600px;
    width: 700px;
    height: 390px;
  }
  .label__brand {
    position: absolute;
    left: 60px;
    top: 520px;
    display: flex;
    align-items: center;
    gap: 10px;
    font-family: "Nunito", sans-serif;
    font-weight: 800;
    font-size: 30px;
    color: var(--brand-green);
  }
  .label__brand-dot {
    width: 22px;
    height: 22px;
    border-radius: 50%;
    background: var(--brand-green);
  }
  .label__photo {
    position: absolute;
    left: 350px;
    top: 395px;
    width: 252px;
    height: 333px;
    background: linear-gradient(160deg, var(--photo-b) 0%, var(--photo-a) 55%, #5d6063 100%);
  }
  .label__copy {
    position: absolute;
    left: 70px;
    top: 752px;
    width: 560px;
    text-align: center;
    font-family: "Quicksand", sans-serif;
    font-weight: 500;
    font-size: 17px;
    line-height: 1.55;
    color: var(--body-text);
  }
</style>
</head>
<body>
  <main class="label">
    <p class="label__tagline">veterinarian formulated</p>
    <h1 class="label__title">SUPPLEMENT<br>FOR CATS</h1>

    <svg class="label__wave" viewBox="0 0 700 390" aria-hidden="true">
      <path d="M0 40 C180 0 420 70 700 10 L700 390 L0 390 Z" fill="var(--wave-light)"/>
      <path d="M0 70 C200 30 430 100 700 40 L700 390 L0 390 Z" fill="var(--wave-deep)"/>
    </svg>

    <div class="label__brand">
      <span class="label__brand-dot"></span>
      <span class="label__brand-name">Corvantis Pets</span>
    </div>

    <div class="label__photo" role="img" aria-label="Photo of a grey tabby cat licking its lips"></div>

    <p class="label__copy">Daily support for joints, coat and digestion, made with gentle natural ingredients your cat will enjoy. Mix one scoop into wet or dry food each day for a healthier and happier companion.</p>
  </main>
</body>
</html>
```